Plastic Business Card for Bookkeeper

We are looking for a simple professional business card design to use for printing on thin frosted plastic (see-through) card stock. Logo and brand guideline documents are attached as well as a photo of our old business card, and another business card example that we like.

Target Market(s)

Small Business

Industry/Entity Type

Bookkeeper

Contact Information for Business Card

Harriet Olsen CPA
Chief Executive Bookkeeper
T. 03 5926 4417
M. 0438 761 205
E. harriet@pinecrestledger.com
W. www.pinecrestledger.com

Font styles to use
Sans Serif

Colors
6b449b
00a990

Requirements
Must have
• Stick with logo colors. Writing should be clear and easy to read and not too cramped together.
Nice to have
• Tag line for back of the card - 'Not your ordinary Bookkeeper'

```html
<!DOCTYPE html>
<html lang="en">
<head>
<meta charset="utf-8">
<title>Pinecrest Ledger – Business Card</title>
<link href="https://fonts.googleapis.com/css2?family=Open+Sans:wght@400;600;700&display=swap" rel="stylesheet">
<style>
  :root {
    --purple: #6b449b;
    --purple-deep: #5a2d83;
    --teal: #00a990;
    --teal-deep: #0b6466;
    --teal-blue: #0e5f78;
    --frost: #efeae2;
    --frost-edge: #d9d2c6;
    --stage: #d8cdbb;
    --light-text: #f3f3f0;
  }
  * { box-sizing: border-box; margin: 0; padding: 0; }
  html, body { width: 1200px; height: 927px; overflow: hidden; }
  body {
    background: var(--stage);
    font-family: "Open Sans", sans-serif;
    position: relative;
  }
  .card {
    position: absolute;
    width: 560px;
    height: 320px;
    background: var(--frost);
    border: 1px solid var(--frost-edge);
    border-radius: 6px;
    overflow: hidden;
    box-shadow: 0 10px 30px rgba(80, 60, 30, 0.18);
  }
  .card--front { left: 50px; top: 110px; }
  .card--back  { left: 590px; top: 497px; }

  /* Front */
  .brand {
    position: absolute;
    left: 0; right: 0; top: 112px;
    display: flex; align-items: center; justify-content: center; gap: 12px;
  }
  .brand__dot {
    width: 18px; height: 18px; border-radius: 50%;
    background: var(--teal-deep);
  }
  .brand__name {
    font-weight: 700; font-size: 32px; color: var(--purple);
    letter-spacing: 0.5px;
  }
  .tagline {
    position: absolute; left: 0; right: 0; top: 176px;
    text-align: center; font-size: 18px; color: var(--teal-deep);
    letter-spacing: 0.3px;
  }

  /* Back */
  .band { position: absolute; inset: 0; width: 100%; height: 100%; }
  .brand-mini {
    position: absolute; left: 34px; top: 48px;
    font-weight: 700; font-size: 20px; color: var(--purple);
  }
  .name-tab {
    position: absolute; right: 0; top: 104px;
    width: 270px; height: 62px;
    background: var(--purple);
    border-radius: 10px 0 0 10px;
    color: var(--light-text);
    text-align: right; padding: 6px 16px 0 0;
  }
  .name-tab__name { font-weight: 700; font-size: 24px; line-height: 28px; }
  .name-tab__role { font-size: 13.5px; line-height: 20px; }
  .contacts {
    position: absolute; right: 16px; top: 190px;
    list-style: none; text-align: right;
    color: var(--light-text); font-size: 14px; line-height: 25px;
  }
  .contacts li { display: flex; justify-content: flex-end; align-items: center; gap: 10px; }
  .contacts svg { width: 13px; height: 13px; fill: none; stroke: var(--light-text); stroke-width: 1.6; }
</style>
</head>
<body>

<section class="card card--front" aria-label="Card front">
  <div class="brand">
    <span class="brand__dot"></span>
    <span class="brand__name">PINECREST LEDGER</span>
  </div>
  <p class="tagline">Not your ordinary Bookkeeper</p>
</section>

<section class="card card--back" aria-label="Card back">
  <svg class="band" viewBox="0 0 560 320" preserveAspectRatio="none" aria-hidden="true">
    <defs>
      <linearGradient id="bandFill" x1="0" y1="0" x2="1" y2="1">
        <stop offset="0" stop-color="#0d6a68"/>
        <stop offset="0.6" stop-color="#0e5f78"/>
        <stop offset="1" stop-color="#0b5f62"/>
      </linearGradient>
    </defs>
    <path d="M0,242 L320,218 C360,214 372,196 386,170 L428,92 C442,70 458,64 480,62 L560,58 L560,320 L0,320 Z"
          fill="url(#bandFill)" stroke="#6b449b" stroke-width="4"/>
  </svg>

  <div class="brand-mini">PINECREST LEDGER</div>

  <div class="name-tab">
    <div class="name-tab__name">Olsen CPA</div>
    <div class="name-tab__role">Chief Executive Bookkeeper</div>
  </div>

  <ul class="contacts">
    <li>03 5926 4417
      <svg viewBox="0 0 14 14"><path d="M3 1.5 L5.5 4 L4 5.5 C5 7.5 6.5 9 8.5 10 L10 8.5 L12.5 11 L11 12.5 C6 12 2 8 1.5 3 Z"/></svg>
    </li>
    <li>0438 761 205
      <svg viewBox="0 0 14 14"><rect x="3.5" y="1" width="7" height="12" rx="1.2"/><line x1="6" y1="11" x2="8" y2="11"/></svg>
    </li>
    <li>harriet@pinecrestledger.com
      <svg viewBox="0 0 14 14"><rect x="1" y="3" width="12" height="8" rx="1"/><path d="M1.5 3.5 L7 8 L12.5 3.5"/></svg>
    </li>
    <li>www.pinecrestledger.com
      <svg viewBox="0 0 14 14"><circle cx="7" cy="7" r="5.8"/><ellipse cx="7" cy="7" rx="2.5" ry="5.8"/><line x1="1.2" y1="7" x2="12.8" y2="7"/></svg>
    </li>
  </ul>
</section>

</body>
</html>
```